Letterhead for financial advisor-insurance agent firm

Our company, Marlowe Thistle Insurance & Investments, is an insurance (health, life, home, auto, etc) and investment brokerage offering a suite of options to meet client needs. We need letterhead that is professional and embodies strength, security and sophistication.

Industry/Entity Type

Investment

```html
<!DOCTYPE html>
<html lang="en">
<head>
<meta charset="utf-8">
<title>Marlowe Thistle Insurance &amp; Investments — Letterhead</title>
<link href="https://fonts.googleapis.com/css2?family=Cormorant+Garamond:wght@500&family=Roboto+Condensed:ital,wght@0,300;1,300&display=swap" rel="stylesheet">
<style>
  :root {
    --navy: #2b2f58;
    --navy-light: #343a68;
    --paper: #ffffff;
    --backdrop: #e6e6e8;
    --ink: #2a2a2a;
    --ink-soft: #555555;
    --rule: #c8c8cc;
    --on-navy: #ffffff;
  }
  * { box-sizing: border-box; margin: 0; padding: 0; }
  html, body { width: 1000px; height: 1200px; overflow: hidden; }
  body { background: var(--backdrop); position: relative; font-family: "Roboto Condensed", "Arial Narrow", sans-serif; }

  .letterhead {
    position: absolute; left: 80px; top: 10px;
    width: 840px; height: 1180px;
    background: var(--paper);
    box-shadow: 0 2px 8px rgba(0,0,0,0.18);
  }
  .letterhead__header {
    position: absolute; left: 0; top: 0; width: 100%; height: 248px;
    background: linear-gradient(135deg, var(--navy) 0%, var(--navy-light) 50%, var(--navy) 100%);
  }
  .brand {
    position: absolute; left: 120px; top: 172px;
    display: flex; align-items: center;
    color: var(--on-navy);
    font-family: "Roboto Condensed", "Arial Narrow", sans-serif; font-weight: 300;
  }
  .brand__square {
    width: 34px; height: 34px; margin-right: 14px;
    border: 2px solid var(--on-navy);
    flex: none;
  }
  .brand__name { font-size: 20px; line-height: 1; white-space: nowrap; }

  .letter { position: absolute; left: 120px; top: 290px; width: 600px; color: var(--ink); }
  .letter__salutation { font-style: italic; font-weight: 300; font-size: 19px; margin-bottom: 14px; }
  .letter__body p { font-weight: 300; font-size: 13.4px; line-height: 20px; margin-bottom: 20px; }
  .letter__body p.gap { margin-top: 38px; }
  .letter__closing { font-style: italic; font-weight: 300; font-size: 16px; color: var(--ink-soft); margin-top: 28px; }

  .footer-rule { position: absolute; left: 120px; top: 968px; width: 596px; height: 1px; background: var(--rule); }
  .contact-list { position: absolute; left: 120px; top: 994px; list-style: none; font-weight: 300; font-size: 12.5px; color: var(--ink-soft); }
  .contact-list li { display: flex; align-items: center; height: 17px; }
  .contact-list svg { width: 11px; height: 11px; margin-right: 9px; fill: var(--ink); }
  .contact-web { position: absolute; right: 124px; top: 1008px; font-weight: 300; font-size: 12.5px; color: var(--ink-soft); }
  .office-block {
    position: absolute; left: 0; width: 100%; top: 1066px; text-align: center; font-style: normal;
    font-family: "Cormorant Garamond", Georgia, serif; font-weight: 500; font-size: 14px; line-height: 18px; color: var(--ink);
  }
</style>
</head>
<body>
  <main class="letterhead">
    <header class="letterhead__header">
      <div class="brand">
        <span class="brand__square"></span>
        <span class="brand__name">Marlowe Thistle Insurance &amp; Investments</span>
      </div>
    </header>

    <section class="letter">
      <p class="letter__salutation">Dear Marlowe</p>
      <div class="letter__body">
        <p>Lorem Ipsum is simply dummy text of the printing and typesetting industry. Lorem Ipsum has been the industry's standard dummy text ever since the 1500s, when an unknown printer took a galley of type and scrambled it to make a type specimen book. It has survived not only five centuries, but also the leap into electronic typesetting, remaining essentially unchanged. It was popularised in the 1960s with the release of Typerow sheets containing Lorem Ipsum passages, and more recently with desktop publishing software like Quillset Pages including versions of Lorem Ipsum.</p>
        <p>It is a long established fact that a reader will be distracted by the readable content of a page when looking at its layout. The point of using Lorem Ipsum is that it has a more-or-less normal distribution of letters, as opposed to using 'Content here, content here', making it look like readable English. Many desktop publishing packages and web page editors now use Lorem Ipsum as their default model text, and a search for 'lorem ipsum' will uncover many web sites still in their infancy. Various versions have evolved over the years, sometimes by accident, sometimes on purpose (injected humour and the like).</p>
        <p class="gap">Contrary to popular belief, Lorem Ipsum is not simply random text. It has roots in a piece of classical Latin literature from 45 BC, making it over 2000 years old. Edwin Harrowgate, a Latin professor at Fenwick-Ashby College in Vermont, looked up one of the more obscure Latin words, consectetur, from a Lorem Ipsum passage, and going through the cites of the word in classical literature, discovered the undoubtable source. Lorem Ipsum comes from sections 1.10.32 and 1.10.33 of "de Finibus Bonorum et Malorum" (The Extremes of Good and Evil) by an old Roman orator, written in 45 BC. This book is a treatise on the theory of ethics, very popular during the Renaissance. The first line of Lorem Ipsum, "Lorem ipsum dolor sit amet..", comes from a line in section 1.10.32.</p>
      </div>
      <p class="letter__closing">Sincerely</p>
    </section>

    <div class="footer-rule"></div>
    <ul class="contact-list">
      <li><svg viewBox="0 0 12 12" aria-hidden="true"><path d="M6 1 L11.5 6 H10 V11 H7.3 V8 H4.7 V11 H2 V6 H0.5 Z"/></svg>11 40512 6638</li>
      <li><svg viewBox="0 0 12 12" aria-hidden="true"><path d="M3.5 0.5 H8.5 A1 1 0 0 1 9.5 1.5 V10.5 A1 1 0 0 1 8.5 11.5 H3.5 A1 1 0 0 1 2.5 10.5 V1.5 A1 1 0 0 1 3.5 0.5 Z M3.7 1.8 V9.2 H8.3 V1.8 Z"/></svg>11 40512 6639</li>
      <li><svg viewBox="0 0 12 12" aria-hidden="true"><path d="M3 1 H9 V4 H11 A0.8 0.8 0 0 1 11.8 4.8 V9 H9.5 V11 H2.5 V9 H0.2 V4.8 A0.8 0.8 0 0 1 1 4 H3 Z M4 2 V4 H8 V2 Z M3.5 7.5 V10 H8.5 V7.5 Z"/></svg>office@marlowethistle.com</li>
    </ul>
    <p class="contact-web">www.marlowethistle.com</p>

    <address class="office-block">
      (912) 555-0187<br>
      advice@marlowethistle.com<br>
      marlowethistle.com
    </address>
  </main>
</body>
</html>
```